Classy business card for accounting firm

We're looking for a new business card for our accounting firm. Our logo was designed by Brandolith, so all of the design info we would like to use has been provided. The specific font provided isn't required to be used.

We want the card to look classy and elegent. Probably more minimalistic, but still with some pops of color.

The options we would like to include on the card are as follows:
1. Main office phone line
2. Direct phone line
3. Email address
4. Website URL
5. Name
6. Title (CEO, President, etc.)
7. Firm Address

The design and card should be double sided!!! The drop down box in the project brief for some reason is defaulting to single sided. Not sure why this is happening.

Thanks!

Contact Information for Business Card

The options we would like to include on the card are as follows: 1. Main office phone line 2. Direct phone line 3. Email address 4. Website URL 5. Name 6. Title (CEO, President, etc.) 7. Firm Address

Requirements
Must have
• Card must be double sided.

```html
<!DOCTYPE html>
<html lang="en">
<head>
<meta charset="utf-8">
<title>Ledgerline Associates — Business Card</title>
<link href="https://fonts.googleapis.com/css2?family=Montserrat:wght@400;500;600;700&display=swap" rel="stylesheet">
<style>
  :root {
    --stage: #3b3b3b;
    --card: #141414;
    --lime: #b3c52b;
    --orange: #f27b1f;
    --white: #f2f2f2;
    --muted: #d6d6d6;
  }
  * { box-sizing: border-box; margin: 0; padding: 0; }
  html, body { width: 1200px; height: 801px; overflow: hidden; }
  body {
    background: radial-gradient(ellipse at 50% 40%, #474747 0%, var(--stage) 70%);
    font-family: "Montserrat", Arial, sans-serif;
    color: var(--white);
    display: flex;
    align-items: center;
    justify-content: center;
    gap: 40px;
  }
  .card {
    position: relative;
    width: 540px;
    height: 309px;
    background: var(--card);
    border-bottom: 3px solid var(--lime);
    box-shadow: 0 18px 40px rgba(0,0,0,.45);
    overflow: hidden;
  }

  /* Contact side */
  .card-front .brand {
    position: absolute;
    left: 34px;
    bottom: 58px;
    width: 230px;
  }
  .brand-mark {
    width: 30px; height: 30px;
    background: var(--orange);
    margin-bottom: 14px;
  }
  .brand-name {
    font-weight: 600;
    font-size: 19px;
    letter-spacing: 1.5px;
    text-transform: uppercase;
    line-height: 1.2;
  }
  .tagline {
    display: flex; align-items: center; gap: 8px;
    margin-top: 6px;
    font-size: 8.5px;
    letter-spacing: 2px;
    text-transform: uppercase;
  }
  .tagline::before, .tagline::after {
    content: ""; height: 1px; background: var(--lime); flex: 1;
  }
  .card-front .divider {
    position: absolute;
    left: 282px; top: 0; bottom: 0;
    width: 1px;
    background: var(--lime);
  }
  .contact {
    position: absolute;
    left: 306px; top: 42px;
    right: 20px;
  }
  .person-name {
    color: var(--lime);
    font-weight: 700;
    font-size: 19px;
    text-transform: uppercase;
    letter-spacing: .5px;
  }
  .person-title { font-size: 11px; margin-top: 2px; }
  .address { font-size: 11px; line-height: 1.45; margin-top: 18px; }
  .lines { list-style: none; margin-top: 18px; font-size: 11px; }
  .lines li { display: flex; align-items: center; gap: 8px; line-height: 1.65; }
  .lines svg { width: 10px; height: 10px; flex: none; fill: var(--orange); }

  /* Brand side */
  .mark-area {
    position: absolute;
    left: 0; top: 0; bottom: 0;
    width: 210px;
    background: linear-gradient(135deg, #0c0c0c 0%, #3a3a3a 55%, #b9b9bd 100%);
  }
  .card-back .brand {
    position: absolute;
    left: 238px; bottom: 70px;
    right: 24px;
  }
  .card-back .brand-name { font-size: 21px; }
  .card-back .tagline { font-size: 9px; }
</style>
</head>
<body>

<section class="card card-front" aria-label="Card front with contact details">
  <div class="brand">
    <div class="brand-mark" aria-hidden="true"></div>
    <div class="brand-name">Ledgerline Associates</div>
    <div class="tagline">Solving Tax Problems</div>
  </div>
  <div class="divider" aria-hidden="true"></div>
  <div class="contact">
    <div class="person-name">Mark Orlen</div>
    <div class="person-title">President</div>
    <div class="address">1180 Harbor Crest Way<br>Seacliff CA 90210</div>
    <ul class="lines">
      <li><svg viewBox="0 0 10 10"><rect x="2" y="0" width="6" height="10" rx="1"/><rect x="3" y="1.5" width="4" height="6" fill="#141414"/></svg>555-240-7310</li>
      <li><svg viewBox="0 0 10 10"><path d="M2 0l2 2.5-1.2 1.3c.7 1.4 1.8 2.5 3.2 3.2L7.3 5.8 10 8l-1.5 2C4 10 0 6 0 1.5z"/></svg>555-240-7310</li>
      <li><svg viewBox="0 0 10 10"><rect x="0" y="2" width="10" height="7"/><path d="M0 2l5 4 5-4" stroke="#141414" fill="none"/></svg>info@LedgerlineAssociates.com</li>
      <li><svg viewBox="0 0 10 10"><circle cx="5" cy="5" r="5"/><path d="M0 5h10M5 0c-2.5 2.5-2.5 7.5 0 10M5 0c2.5 2.5 2.5 7.5 0 10" stroke="#141414" stroke-width=".8" fill="none"/></svg>www.LedgerlineAssociates.com</li>
    </ul>
  </div>
</section>

<section class="card card-back" aria-label="Card back with firm name">
  <div class="mark-area" role="img" aria-label="Large glossy brand mark decoration"></div>
  <div class="brand">
    <div class="brand-name">Ledgerline Associates</div>
    <div class="tagline">Solving Tax Problems</div>
  </div>
</section>

</body>
</html>
```